Template für Webova-Page
Zielgruppe
Geschlecht: ca. 90% Männlich
Alter: ca. 30-60 Jahre
höheres Einkommen, höhere Bildung
Aufgabenstellung
FORNVALT ist ein Netzwerk von Maßschuhmachern. Die Schuhmacher werden auf der Webseite gefunden und es wird ein Eindruck der Möglichkeiten des Maßschuhmachens vermittelt.
Aufgrund der offenen Struktur arbeiten wir derzeit mit Webova, damit jeder Schuhmacher die Möglichkeit hat, Inhalte einzustellen, zu pflegen und zu aktualisieren.
Webova scheint für diese Zwecke gut geeignet, hat aber kein adäquates Standard-Layout.
ES GEHT NUR UM DAS WEBDESIGN, NICHT UM DIE IMPLEMENTIERUNG!

```html
<!DOCTYPE html>
<html lang="de">
<head>
<meta charset="utf-8">
<title>FORNVALT – Unser Produkt</title>
<link href="https://fonts.googleapis.com/css2?family=Arimo:wght@400;700&display=swap" rel="stylesheet">
<style>
:root{
  --bg:#0f0e0d;
  --bg-light:#2b2824;
  --grain-light:rgba(255,255,255,.045);
  --grain-dark:rgba(0,0,0,.35);
  --panel:rgba(38,35,32,.72);
  --nav-top:#2e2c2a;
  --nav-bottom:#121110;
  --gold:#d4a83c;
  --text:#f2efe8;
  --bar:#3a3836;
  --white:#ffffff;
  --toggle:#e6e4e0;
  --loafer-light:#f3f4f4;
  --loafer-red:#6b2824;
  --loafer-tan:#c89b73;
  --boot-light:#f4f4f3;
  --boot-black:#141414;
}
*{margin:0;padding:0;box-sizing:border-box}
html,body{width:1200px;height:931px;overflow:hidden}
body{
  position:relative;
  background:
    radial-gradient(circle at 30% 30%,var(--grain-light) 0 1.2px,transparent 1.8px) 0 0/7px 6px,
    radial-gradient(circle at 70% 60%,var(--grain-dark) 0 1.6px,transparent 2.4px) 2px 3px/9px 8px,
    radial-gradient(circle at 50% 50%,var(--grain-light) 0 2px,transparent 3px) 4px 1px/13px 11px,
    radial-gradient(circle at 40% 60%,var(--grain-dark) 0 2.5px,transparent 4px) 1px 5px/17px 15px,
    radial-gradient(ellipse at 60% 35%,var(--bg-light) 0%,#1a1816 45%,var(--bg) 85%);
  font-family:"Arimo",Arial,sans-serif;
  color:var(--text);
  letter-spacing:.05em;
}
.brand{
  position:absolute;left:19px;top:22px;width:147px;height:141px;
  background:linear-gradient(180deg,#1d1b19 0%,#0b0a09 100%);
  display:flex;flex-direction:column;align-items:center;justify-content:flex-start;padding-top:12px;gap:6px;
}
.brand-dot{width:34px;height:34px;border-radius:50%;border:2px solid var(--gold)}
.brand-name{font-size:22px;font-weight:700;color:var(--gold);letter-spacing:.02em}
.topnav{
  position:absolute;left:182px;top:34px;width:980px;height:65px;
  background:linear-gradient(180deg,var(--nav-top),var(--nav-bottom));
  border-radius:4px;
}
.topnav a{position:absolute;top:24px;font-size:15px;color:var(--text);text-decoration:none;letter-spacing:.06em}
.topnav a.active{color:var(--gold)}
.main{
  position:absolute;left:182px;top:110px;width:980px;height:840px;
  background:var(--panel);border-radius:4px 4px 0 0;
}
.sidebar{position:absolute;left:0;top:0;width:218px;height:100%;border-right:1px solid #0c0b0a}
.subnav a{position:absolute;left:27px;font-size:15px;color:var(--text);text-decoration:none;letter-spacing:.06em}
.subnav a.active{color:var(--gold)}
.partner-box{
  position:absolute;left:11px;top:192px;width:197px;height:66px;background:var(--white);
  border:1px solid #999;display:flex;align-items:center;gap:8px;padding-left:18px;
}
.partner-box .dot{width:24px;height:24px;border-radius:50%;background:#2aa3dc}
.partner-box span{font-size:26px;color:#2aa3dc;letter-spacing:0}
.view-toggle{
  position:absolute;left:16px;top:297px;width:173px;height:34px;border-radius:4px;
  background:var(--toggle);font-size:10px;color:#555;
  display:flex;align-items:center;justify-content:center;letter-spacing:.06em;
}
.view-toggle a{color:var(--gold);margin:0 3px;text-decoration:underline}
.side-title{position:absolute;left:16px;top:365px;width:160px;font-size:13px;font-weight:700;color:var(--gold);line-height:21px;letter-spacing:.07em}
.side-text{position:absolute;left:16px;top:432px;width:172px;font-size:13px;line-height:21px;letter-spacing:.07em}
.content h2{position:absolute;left:201px;font-size:19px;font-weight:400;color:var(--gold);letter-spacing:.03em}
.gallery{position:absolute;left:201px;width:696px;background:#1c1b1a}
.photo-loafer{
  position:absolute;
  background:
    radial-gradient(ellipse at 28% 60%,var(--loafer-red) 0%,rgba(107,40,36,.7) 22%,transparent 42%),
    radial-gradient(ellipse at 66% 50%,var(--loafer-tan) 0%,rgba(200,155,115,.75) 22%,transparent 42%),
    linear-gradient(180deg,var(--loafer-light),#e9e8e6);
}
.photo-boot{
  position:absolute;
  background:
    radial-gradient(ellipse at 80% 70%,var(--boot-black) 0%,rgba(20,20,20,.8) 25%,transparent 45%),
    radial-gradient(ellipse at 30% 90%,#1e1e1e 0%,rgba(30,30,30,.7) 25%,transparent 45%),
    linear-gradient(180deg,var(--boot-light),#e3e3e1);
}
.controls{position:absolute;left:0;width:696px;height:43px;background:rgba(58,56,54,.92);border-top:1px solid #ddd}
.controls svg{position:absolute}
.thumb{position:absolute;top:6px;width:22px;height:31px;background:linear-gradient(135deg,#eee,#6b3a2c)}
.g2bar{position:absolute;left:0;top:0;width:696px;height:31px;background:var(--bar)}
</style>
</head>
<body>
<div class="brand"><div class="brand-dot"></div><div class="brand-name">FORNVALT</div></div>

<nav class="topnav">
  <a style="left:28px">Start</a>
  <a style="left:104px">Kontakt</a>
  <a class="active" style="left:202px">Unser Produkt</a>
  <a style="left:355px">Preise</a>
  <a style="left:444px">Partner</a>
  <a style="left:540px">Ihr Weg zum Maßschuh</a>
</nav>

<div class="main">
  <aside class="sidebar">
    <nav class="subnav">
      <a class="active" style="top:37px">Passform</a>
      <a style="top:76px">Aussehen</a>
      <a style="top:114px">Handwerk</a>
      <a style="top:153px">Pflege</a>
    </nav>
    <div class="partner-box"><div class="dot"></div><span>Webova</span></div>
    <div class="view-toggle">Ansicht: <a>Galerie</a>|<a>Liste</a></div>
    <div class="side-title">Platz für weitere Inhaltselement</div>
    <p class="side-text">Es erscheint unterhalb des Menüs der zweiten Ebene. Die Webova Werbebox darüber bitte wegdenken.</p>
  </aside>

  <section class="content">
    <h2 style="top:20px">Maßschuhe auf Grundlage unseres Schaftkataloges</h2>
    <div class="gallery" style="top:54px;height:391px">
      <div class="photo-loafer" role="img" aria-label="Bordeauxroter Penny-Loafer aus Leder mit Ledersohle, auf hellem Grund" style="left:13px;top:0;width:670px;height:348px"></div>
      <div class="controls" style="top:348px">
        <svg style="left:12px;top:12px" width="20" height="20" viewBox="0 0 20 20"><circle cx="10" cy="10" r="9" fill="#9a9793"/><text x="10" y="14.5" font-size="13" font-weight="700" text-anchor="middle" fill="#3a3836" font-family="Arial">?</text></svg>
        <svg style="left:43px;top:14px" width="22" height="16" viewBox="0 0 22 16" fill="#9a9793"><rect x="0" y="0" width="6" height="4"/><rect x="8" y="0" width="6" height="4"/><rect x="16" y="0" width="6" height="4"/><rect x="0" y="6" width="6" height="4"/><rect x="8" y="6" width="6" height="4"/><rect x="16" y="6" width="6" height="4"/><rect x="0" y="12" width="6" height="4"/><rect x="8" y="12" width="6" height="4"/><rect x="16" y="12" width="6" height="4"/></svg>
        <div class="thumb" style="left:126px"></div>
        <div class="thumb" style="left:150px;border:1px solid #bbb"></div>
        <div class="thumb" style="left:172px;background:linear-gradient(135deg,#eee,#111)"></div>
        <svg style="left:636px;top:13px" width="20" height="17" viewBox="0 0 20 17" fill="none" stroke="#cfccc8" stroke-width="2"><rect x="1" y="3" width="15" height="13"/><path d="M9 9 L18 1 M12 1 H18 V7"/></svg>
        <svg style="left:668px;top:13px" width="12" height="17" viewBox="0 0 12 17" fill="#cfccc8"><rect x="1" y="1" width="3" height="15"/><rect x="8" y="1" width="3" height="15"/></svg>
      </div>
    </div>

    <h2 style="top:468px">Maßschuhe nach individueller Vorgabe</h2>
    <div class="gallery" style="top:502px;height:340px">
      <div class="g2bar"></div>
      <div class="photo-boot" role="img" aria-label="Schwarze Stiefelette mit Reißverschluss und schwarzer Sohle, auf hellem Grund" style="left:0;top:31px;width:696px;height:309px"></div>
    </div>
  </section>
</div>
</body>
</html>
```